Brightwell Settlement Brochure/Flyer Revisions

Improve the current design and over all look for Tri-Fold brochure and 8 x 11 flyer along with update the text and view picture substitutions.

Target Market(s)

Currently our brochure is geared more towards the Cancer Patient, and less Senior.
I want to take the new revisions text, or new message, and incorporate it into the new designed brochure and flyer. I want a nice picture of a senior or couple to be primary view shot and the cancer patients secondary.
Please visit our website; www.brightwellsettlements.org

Requirements
Must have
• we want all Seniors and Cancer Patients that own a life insurance policy, group or individual to call us. We want the consumer to be educated and know their rights.
Brightwell Settlements will be there ADVOCATE and Financial RESOURCE

```html
<!DOCTYPE html>
<html lang="en">
<head>
<meta charset="utf-8">
<title>Brightwell Settlements – Seniors &amp; Patients Financial Resource Flyer</title>
<link rel="stylesheet" href="https://fonts.googleapis.com/css2?family=Arvo:wght@400;700&family=Questrial&display=swap">
<style>
  :root {
    --charcoal: #4a4544;
    --teal: #3ab1c4;
    --navy: #0c1836;
    --navy-soft: #1a2a55;
    --navy-text: #1d2b5c;
    --green: #8cc63f;
    --lime: #a9d13b;
    --white: #ffffff;
    --ink: #1b1b1f;
  }
  * { margin: 0; padding: 0; box-sizing: border-box; }
  html, body { width: 1200px; height: 920px; overflow: hidden; background: var(--charcoal); }
  body { font-family: "Arvo", "Rockwell", serif; }

  .flyer { position: relative; width: 1200px; height: 920px; background: var(--charcoal); overflow: hidden; }

  /* Hero photo band */
  .hero-photo {
    position: absolute; left: 28px; top: 0; width: 758px; height: 344px;
    background: linear-gradient(100deg, #e9eef1 0%, #dfe7ec 35%, #c9d6dc 50%, #a08371 64%, #6b4a38 80%, #a9b8b4 100%);
  }
  .hero-divider { position: absolute; left: 400px; top: 0; width: 1px; height: 344px; background: rgba(255,255,255,.5); }

  /* Colour bars */
  .colour-bars { position: absolute; left: 28px; top: 366px; display: flex; gap: 3px; }
  .colour-bars span { display: block; width: 84px; height: 20px; }
  .bar-green { background: var(--green); }
  .bar-teal { background: var(--teal); }
  .bar-lime { background: var(--lime); }

  /* Left panel */
  .money-panel {
    position: absolute; left: 25px; top: 413px; width: 345px; height: 507px;
    background: linear-gradient(180deg, var(--navy) 0%, var(--navy-soft) 100%);
  }
  .money-title {
    position: absolute; left: 35px; top: 427px;
    font-weight: 400; font-size: 33px; color: var(--teal); letter-spacing: .2px; white-space: nowrap;
  }
  .couple-photo {
    position: absolute; left: 0; top: 568px; width: 250px; height: 352px;
    background: linear-gradient(160deg, rgba(40,40,46,.95) 0%, #5a4a42 40%, #c9b4a4 60%, #e8e4e0 85%, #f2f2f2 100%);
  }
  .money-questions span {
    position: absolute; left: var(--x); top: var(--y); white-space: nowrap;
    font-size: 11.6px; line-height: 1; color: var(--white);
  }

  /* Middle panel */
  .help-panel {
    position: absolute; left: 401px; top: 344px; width: 400px; height: 576px;
    background: var(--teal); color: var(--white);
  }
  .help-headline { position: absolute; left: 12px; top: 12px; font-size: 66px; font-weight: 400; line-height: 1; }
  .help-lead { position: absolute; left: 12px; top: 86px; width: 378px; font-size: 11.2px; line-height: 1.4; }
  .help-subhead {
    position: absolute; left: 20px; top: 142px; white-space: nowrap;
    font-family: "Questrial", "Helvetica", sans-serif; font-size: 60px; line-height: 1;
  }
  .help-intro { position: absolute; left: 12px; top: 214px; width: 380px; font-size: 11.2px; line-height: 1.4; }
  .help-points { position: absolute; left: 16px; top: 300px; width: 378px; font-size: 11.2px; line-height: 1.45; }
  .help-points p { margin-bottom: 12px; }
  .help-points strong { font-weight: 400; color: var(--navy-text); }

  /* Reply card */
  .reply-card { position: absolute; left: 828px; top: 0; width: 345px; height: 920px; background: var(--teal); }
  .reply-card-inner {
    position: absolute; left: 0; top: 920px; width: 920px; height: 345px;
    transform-origin: 0 0; transform: rotate(-90deg); color: var(--ink);
  }
  .reply-row {
    position: absolute; left: 30px; display: flex; align-items: flex-end;
    font-size: 19px; line-height: 1; white-space: nowrap;
  }
  .reply-intro { top: 24px; font-size: 14.5px; font-weight: 700; }
  .field { display: flex; align-items: flex-end; }
  .field-line { display: inline-block; border-bottom: 1px solid var(--ink); height: 1px; margin: 0 8px 3px 6px; }
  .reply-notice { top: 298px; font-size: 19px; letter-spacing: .3px; }
  .reply-disclaimer { top: 324px; font-size: 12.5px; }

  .brand-mark {
    position: absolute; left: 740px; top: 60px; display: flex; align-items: center; gap: 8px;
    font-weight: 700; color: var(--navy-text); font-size: 15px; line-height: 1.1;
  }
  .brand-dot { width: 22px; height: 22px; border-radius: 50%; background: var(--navy-text); flex: none; }
</style>
</head>
<body>
<main class="flyer">
  <div class="hero-photo" role="img" aria-label="Photo of a smiling senior man with a caring nurse's hand on his shoulder"></div>
  <div class="hero-divider"></div>

  <div class="colour-bars">
    <span class="bar-green"></span><span class="bar-teal"></span><span class="bar-lime"></span><span class="bar-teal"></span>
  </div>

  <section class="money-panel"></section>
  <h2 class="money-title">It’s Your Money.....</h2>
  <div class="couple-photo" role="img" aria-label="Photo of a man kissing the forehead of a woman undergoing cancer treatment"></div>
  <div class="money-questions">
    <span style="--x:48px;--y:476px">Why are policy owners rarely told they may be</span>
    <span style="--x:48px;--y:497px">entitled to additional cash benefits from a life</span>
    <span style="--x:48px;--y:519px">insurance policy?</span>
    <span style="--x:106px;--y:541px">Why are bankruptcy rates among seniors</span>
    <span style="--x:139px;--y:563px">and cancer patients more than</span>
    <span style="--x:153px;--y:585px">double that of the general</span>
    <span style="--x:153px;--y:607px">population?</span>
    <span style="--x:152px;--y:628px">Why do so many seniors and</span>
    <span style="--x:212px;--y:650px">patients receiving care</span>
    <span style="--x:226px;--y:672px">feel uncomfortable</span>
    <span style="--x:230px;--y:694px">discussing the</span>
    <span style="--x:230px;--y:716px">subject of money and</span>
    <span style="--x:230px;--y:738px">the overwhelming</span>
    <span style="--x:230px;--y:760px">effects it has on the</span>
    <span style="--x:242px;--y:782px">entire family?</span>
  </div>

  <section class="help-panel">
    <h1 class="help-headline">Everyone</h1>
    <p class="help-lead">who owns a life insurance policy, group or individual, deserves to know their rights and have access to FINANCIAL SUPPORT SERVICES that improve quality of life.</p>
    <h2 class="help-subhead">We can Help</h2>
    <p class="help-intro">As your ADVOCATE and FINANCIAL RESOURCE, Brightwell Settlements gives seniors and patients the guidance to maximize their insurance benefits and explore the FINANCIAL OPTIONS AVAILABLE.</p>
    <div class="help-points">
      <p><strong>ARE YOU</strong> a senior who owns an individual or group life insurance policy that is still in force?</p>
      <p><strong>HAVE YOU</strong> been diagnosed with a life threatening illness and are insured by a life or group insurance policy?</p>
      <p><strong>CALL A FAMILY SERVICE COUNSELOR</strong> today to check your eligibility and ask about our <strong>FREE REFERRAL SERVICE</strong> that connects seniors and patients with non profit organizations and Financial Alternatives.</p>
    </div>
  </section>

  <aside class="reply-card">
    <div class="reply-card-inner">
      <p class="reply-row reply-intro">Yes, I would like to know my options and hear about the FREE REFERRAL SERVICE you offer</p>
      <div class="reply-row" style="top:60px"><span class="field">Name:<span class="field-line" style="width:640px"></span></span></div>
      <div class="reply-row" style="top:100px"><span class="field">Address:<span class="field-line" style="width:610px"></span></span></div>
      <div class="reply-row" style="top:140px">
        <span class="field">City:<span class="field-line" style="width:120px"></span></span>
        <span class="field">State:<span class="field-line" style="width:120px"></span></span>
        <span class="field">Zip Code:<span class="field-line" style="width:222px"></span></span>
      </div>
      <div class="reply-row" style="top:180px"><span class="field">E-mail address:<span class="field-line" style="width:530px"></span></span></div>
      <div class="reply-row" style="top:220px"><span class="field">Phone :<span class="field-line" style="width:605px"></span></span></div>
      <div class="reply-row" style="top:258px"><span class="field">Insurance Co:<span class="field-line" style="width:560px"></span></span></div>
      <p class="reply-row reply-notice">ALL COMMUNICATION WILL BE KEPT STRICTLY CONFIDENTIAL</p>
      <p class="reply-row reply-disclaimer">Brightwell Settlements services are not available to all policy owners and certain restrictions may apply.</p>
      <div class="brand-mark"><span class="brand-dot"></span><span>Brightwell<br>Settlements</span></div>
    </div>
  </aside>
</main>
</body>
</html>
```